Agriculture Magazine Print Ad for Farm magazines to drive traffic to website

We require a print ad designed for publication in an agriculture magazine.
This print ad will be used in multiple publications to represent our company brand and give our core message to customers.

our website is Tarvelbeam.com we provide industrial lighting solutions to farm and commercial businesses.

Please advise if any additional files or documents are required

I have included some ads from these magazines that our competitors have published. And some images of our products and a few previous installations.

Target Market(s)

Blue Collar business Owners and Farm owners

Industry/Entity Type

Farm Equipment

Requirements
Must have
• Logo
Product Images
Toll Free Number 1-800-555-0147
Free Shipping on Orders over $249
Located in Larkmoor LM

High res quality
Ability to scale ad to various sizes
1/2 page, 1/4 page
Vertical ad 1/4 and full page, horizontal 1/2 page ad.
Email address : Support@tarvelbeam.com
Website address Tarvelbeam.com
Nice to have
• images of previous projects

Color Scheme from website

Various ad design sizes per attached image
Full page 10 1/4" x 7"
Half page Horizontal 7"x5"
1/4 page Vertical 3 3/8 x 5"
1/4 Page Horizintal 7" 2 3/8"

```html
<!DOCTYPE html>
<html lang="en">
<head>
<meta charset="utf-8">
<title>Tarvelbeam – LED Garage &amp; Industrial Shop Lighting</title>
<link href="https://fonts.googleapis.com/css2?family=Montserrat:wght@400;500;600;700;800&display=swap" rel="stylesheet">
<style>
:root{
  --red:#d42027;
  --red-soft:#e4575c;
  --ink:#161616;
  --text:#3a3a3a;
  --page:#f5f5f5;
  --band:#e5e5e5;
  --backdrop:#dcdcda;
  --gold:#c9a227;
}
*{box-sizing:border-box;margin:0;padding:0}
html,body{width:1200px;height:861px;overflow:hidden;background:var(--backdrop);font-family:'Montserrat',sans-serif;color:var(--ink)}
.spread{position:relative;width:1200px;height:861px}
.page{position:absolute;top:42px;width:570px;height:776px;background:var(--page);overflow:hidden}
.page--ad{left:22px}
.page--back{left:608px;background:#f8f8f8}

/* brand */
.brand{display:flex;align-items:center;gap:7px}
.brand__mark{width:14px;height:14px;background:var(--red)}
.brand__name{font-weight:800;color:var(--red);letter-spacing:.5px;font-size:22px}

/* hero */
.hero{position:absolute;left:0;top:0;width:570px;height:298px}
.hero__photo{position:absolute;inset:0;background:linear-gradient(180deg,#cfd3d6 0%,#e9ecee 35%,#dfe2e4 75%,#bfc2c3 100%)}
.hero .brand{position:absolute;left:24px;top:24px}
.headline{position:absolute;left:0;right:0;top:96px;text-align:center;font-weight:800;line-height:1}
.headline__top{display:block;font-size:29px;color:var(--ink)}
.headline__bottom{display:block;font-size:29px;color:var(--red);margin-top:2px}
.certs{display:flex;gap:12px;justify-content:center;margin-top:12px}
.cert{width:16px;height:16px;border-radius:50%;background:#4a4a4a}
.cert--gold{background:var(--gold)}
.seal{position:absolute;right:36px;top:208px;width:110px;height:110px}

/* products */
.products{position:absolute;left:16px;right:10px;top:330px;display:grid;grid-template-columns:repeat(4,1fr);row-gap:26px;column-gap:12px}
.product__img{height:82px;width:92px;margin:0 0 14px 10px;border-radius:8px;background:radial-gradient(circle at 50% 45%,#c9ccce 0%,#6b6e70 60%,#f5f5f5 100%)}
.product__title{font-size:10px;font-weight:700;text-transform:uppercase;white-space:nowrap;letter-spacing:-.2px}
.product__desc{font-size:7.4px;color:var(--text);line-height:1.3;margin-top:4px;width:120px}
.product__price{display:inline-block;margin-top:8px;background:var(--red);color:#fff;font-size:8.5px;font-weight:600;padding:4px 8px}

/* footer */
.footer{position:absolute;left:0;right:0;bottom:0;height:96px;background:var(--band);display:flex;align-items:center;padding:0 16px 0 20px;justify-content:space-between}
.footer__brand .brand__name{font-size:21px}
.footer__url{font-size:9px;font-weight:600;margin:3px 0 0 21px}
.contact__label{font-size:11.5px;font-weight:600}
.contact__phone{font-size:19px;font-weight:800;color:var(--red);line-height:1.15}
.contact__mail{font-size:8.5px;font-weight:600}
.shipping{font-size:11px;line-height:1.25}
.shipping__top{font-weight:600;color:#555}
.shipping__main{font-size:15px;font-weight:500}
.shipping__main strong{color:var(--red);font-weight:700}
.shipping__loc span{color:var(--red)}

/* back cover */
.page--back .brand{position:absolute;left:0;right:0;top:150px;justify-content:center}
.page--back .brand__name{font-size:26px}
.back__headline{position:absolute;left:0;right:0;top:352px;text-align:center;font-weight:800;line-height:1}
.back__headline .headline__top{font-size:30px}
.back__headline .headline__bottom{font-size:30px;color:var(--red-soft)}
.back__contact{position:absolute;left:0;right:0;top:630px;text-align:center}
.back__contact .contact__label{font-size:11px}
.back__contact .contact__phone{font-size:17px}
.back__contact .contact__mail{font-size:7.5px}
.back__certs{position:absolute;left:0;right:0;top:725px}
</style>
</head>
<body>
<main class="spread">

  <section class="page page--ad">
    <header class="hero">
      <div class="hero__photo" role="img" aria-label="Photo of a bright metal-clad shop interior with LED ceiling lights, red shelving, a ride-on mower and a ladder"></div>
      <div class="brand"><span class="brand__mark"></span><span class="brand__name">TARVELBEAM</span></div>
      <h1 class="headline">
        <span class="headline__top">LED GARAGE &amp; INDUSTRIAL</span>
        <span class="headline__bottom">SHOP LIGHTING</span>
        <span class="certs"><span class="cert"></span><span class="cert"></span><span class="cert"></span><span class="cert cert--gold"></span></span>
      </h1>
    </header>

    <svg class="seal" viewBox="0 0 110 110" aria-label="60 day money back guarantee">
      <circle cx="55" cy="55" r="54" fill="#f3c6c8"/>
      <circle cx="55" cy="55" r="48" fill="#fff"/>
      <circle cx="55" cy="55" r="43" fill="#e35a60"/>
      <text x="55" y="38" text-anchor="middle" fill="#fff" font-family="Montserrat, sans-serif" font-size="7" font-weight="600">MONEY BACK</text>
      <rect x="17" y="45" width="76" height="22" fill="none" stroke="#fff" stroke-width="1.2"/>
      <text x="55" y="62" text-anchor="middle" fill="#fff" font-family="Montserrat, sans-serif" font-size="15" font-weight="700">60 DAY</text>
      <text x="55" y="80" text-anchor="middle" fill="#fff" font-family="Montserrat, sans-serif" font-size="6.5" font-weight="600">GUARANTEE</text>
    </svg>

    <div class="products">
      <article class="product"><div class="product__img" role="img" aria-label="UFO high bay industrial LED fixture"></div><h2 class="product__title">Industrial LED</h2><p class="product__desc">Sed ut perspiciatis unde omnis iste natus error sit voluptatem</p><span class="product__price">From $239.97</span></article>
      <article class="product"><div class="product__img" role="img" aria-label="Three-panel LED garage light"></div><h2 class="product__title">LED Garage Lights</h2><p class="product__desc">Sed ut perspiciatis unde omnis iste natus error sit voluptatem</p><span class="product__price">From $89.97</span></article>
      <article class="product"><div class="product__img" role="img" aria-label="Industrial LED corn bulb"></div><h2 class="product__title">Industrial LED</h2><p class="product__desc">Sed ut perspiciatis unde omnis iste natus error sit voluptatem</p><span class="product__price">From $44.97</span></article>
      <article class="product"><div class="product__img" role="img" aria-label="LED corn bulb"></div><h2 class="product__title">LED Corn Bulbs</h2><p class="product__desc">Sed ut perspiciatis unde omnis iste natus error sit voluptatem</p><span class="product__price">From $44.97</span></article>
      <article class="product"><div class="product__img" role="img" aria-label="LED wall pack fixture for parking lots"></div><h2 class="product__title">LED Parking Lot Lights</h2><p class="product__desc">Sed ut perspiciatis unde omnis iste natus error sit voluptatem</p><span class="product__price">From $239.97</span></article>
      <article class="product"><div class="product__img" role="img" aria-label="LED area yard light with photocell"></div><h2 class="product__title">LED Yard Lights</h2><p class="product__desc">Sed ut perspiciatis unde omnis iste natus error sit voluptatem</p><span class="product__price">From $89.97</span></article>
      <article class="product"><div class="product__img" role="img" aria-label="LED shoebox area light"></div><h2 class="product__title">High Bay LED Lights</h2><p class="product__desc">Sed ut perspiciatis unde omnis iste natus error sit voluptatem</p><span class="product__price">From $44.97</span></article>
      <article class="product"><div class="product__img" role="img" aria-label="Round LED retrofit lamp"></div><h2 class="product__title">LED Wall Packs</h2><p class="product__desc">Sed ut perspiciatis unde omnis iste natus error sit voluptatem</p><span class="product__price">From $44.97</span></article>
    </div>

    <footer class="footer">
      <div class="footer__brand">
        <div class="brand"><span class="brand__mark"></span><span class="brand__name">TARVELBEAM</span></div>
        <p class="footer__url">Tarvelbeam.com</p>
      </div>
      <div class="contact">
        <p class="contact__label">Toll Free Number</p>
        <p class="contact__phone">1-800-555-0147</p>
        <p class="contact__mail">Support@tarvelbeam.com</p>
      </div>
      <div class="shipping">
        <p class="shipping__top">Free Shipping</p>
        <p class="shipping__main">On Orders <strong>Over $249</strong></p>
        <p class="shipping__loc">Located in <span>Larkmoor LM</span></p>
      </div>
    </footer>
  </section>

  <section class="page page--back">
    <div class="brand"><span class="brand__mark"></span><span class="brand__name">TARVELBEAM</span></div>
    <h2 class="back__headline">
      <span class="headline__top">LED GARAGE &amp; INDUSTRIAL</span>
      <span class="headline__bottom">SHOP LIGHTING</span>
    </h2>
    <div class="back__contact">
      <p class="contact__label">Toll Free Number</p>
      <p class="contact__phone">1-800-555-0147</p>
      <p class="contact__mail">Support@tarvelbeam.com</p>
    </div>
    <div class="certs back__certs"><span class="cert"></span><span class="cert"></span><span class="cert"></span><span class="cert cert--gold"></span></div>
  </section>

</main>
</body>
</html>
```